Updated DJ business Card showing other businesses

DJ Kestro offers professional mobile dj services including DJ. MC. Karaoke.
Hushwave (will attach logo)
I also offer a 360 Photo Booth.

Contact info:
(555) 314-7720
lenny.corbitt@mailvane.net
Social Media @DJKestroBPZ

```html
<!DOCTYPE html>
<html lang="en">
<head>
<meta charset="utf-8">
<title>DJ Kestro – Business Card</title>
<link rel="stylesheet" href="https://fonts.googleapis.com/css2?family=Montserrat:wght@400;900&family=Oswald:wght@600&display=swap">
<style>
  :root {
    --stage: #3a3a3a;
    --paper: #ffffff;
    --ink: #111111;
    --night: #0b0b0b;
    --accent: #ef1a48;
    --accent-deep: #c8203f;
  }
  * { box-sizing: border-box; margin: 0; padding: 0; }
  html, body { width: 1200px; height: 1200px; overflow: hidden; }
  body {
    background: var(--stage);
    font-family: "Montserrat", Arial, sans-serif;
    display: flex;
    flex-direction: column;
    align-items: center;
    justify-content: center;
    gap: 44px;
  }
  .card {
    position: relative;
    width: 920px;
    height: 526px;
    border-radius: 40px;
    overflow: hidden;
    box-shadow: 0 14px 30px rgba(0,0,0,.35);
  }

  /* Front */
  .card--front { background: var(--paper); color: var(--ink); }
  .front-art {
    position: absolute;
    left: 0; top: 0;
    width: 440px; height: 526px;
  }
  .front-info {
    position: absolute;
    left: 480px; top: 70px;
    width: 400px;
  }
  .brand-name {
    font-weight: 900;
    font-size: 64px;
    line-height: 1;
    letter-spacing: -1px;
    color: var(--ink);
    text-transform: uppercase;
    margin-bottom: 30px;
  }
  .contact-list { list-style: none; }
  .contact-item {
    display: flex;
    align-items: center;
    gap: 12px;
    font-size: 23px;
    font-weight: 400;
    line-height: 1.55;
    white-space: nowrap;
  }
  .contact-icon { width: 24px; height: 24px; flex: none; }
  .social-mark {
    width: 22px; height: 22px;
    border: 2.5px solid var(--accent);
    border-radius: 5px;
    flex: none;
  }
  .service-lines {
    position: absolute;
    right: 44px; bottom: 52px;
    text-align: right;
    font-family: "Oswald", "Arial Narrow", sans-serif;
    font-weight: 600;
    font-size: 26px;
    line-height: 1.25;
    text-transform: uppercase;
    color: var(--ink);
    white-space: nowrap;
  }
  .dot { color: var(--accent); padding: 0 4px; }

  /* Back */
  .card--back { background: var(--night); color: var(--paper); }
  .back-logo {
    position: absolute;
    left: 0; right: 0; top: 120px;
    text-align: center;
  }
  .back-logo .brand-name {
    color: var(--paper);
    font-size: 96px;
    margin-bottom: 34px;
  }
  .partner-mark {
    display: inline-flex;
    align-items: center;
    gap: 14px;
    font-weight: 900;
    font-size: 38px;
    text-transform: uppercase;
    color: var(--paper);
  }
  .partner-dot {
    width: 30px; height: 30px;
    border-radius: 50%;
    background: var(--paper);
  }
  .equalizer {
    position: absolute;
    left: 0; bottom: 0;
    width: 920px; height: 170px;
  }
</style>
</head>
<body>

  <section class="card card--front" aria-label="Business card front">
    <svg class="front-art" viewBox="0 0 440 526" role="img" aria-label="Large rhino head illustration in red">
      <path d="M0 40 C150 58 290 115 360 220 C400 290 415 400 420 526 L0 526 Z" fill="var(--accent)"/>
    </svg>

    <div class="front-info">
      <div class="brand-name">DJ Kestro</div>
      <ul class="contact-list">
        <li class="contact-item">
          <svg class="contact-icon" viewBox="0 0 24 24" aria-hidden="true">
            <path d="M6.6 10.8a15 15 0 0 0 6.6 6.6l2.2-2.2a1 1 0 0 1 1-.25 11.4 11.4 0 0 0 3.6.6 1 1 0 0 1 1 1V20a1 1 0 0 1-1 1A17 17 0 0 1 3 4a1 1 0 0 1 1-1h3.5a1 1 0 0 1 1 1c0 1.25.2 2.45.6 3.6a1 1 0 0 1-.25 1z" fill="var(--accent)"/>
          </svg>
          (555) 314-7720
        </li>
        <li class="contact-item">
          <svg class="contact-icon" viewBox="0 0 24 24" aria-hidden="true">
            <rect x="2" y="5" width="20" height="14" rx="1.5" fill="var(--accent)"/>
            <path d="M2.5 6 12 13l9.5-7" fill="none" stroke="var(--paper)" stroke-width="1.6"/>
          </svg>
          lenny.corbitt@mailvane.net
        </li>
        <li class="contact-item">
          <span class="social-mark" aria-hidden="true"></span>
          @DJKestroBPZ
        </li>
      </ul>
    </div>

    <div class="service-lines">
      <div>Mobile DJ Services</div>
      <div>DJ<span class="dot">•</span>MC<span class="dot">•</span>Karaoke<span class="dot">•</span>360 Photo Booth</div>
    </div>
  </section>

  <section class="card card--back" aria-label="Business card back">
    <div class="back-logo">
      <div class="brand-name">DJ Kestro</div>
      <div class="partner-mark"><span class="partner-dot" aria-hidden="true"></span>Hushwave</div>
    </div>

    <svg class="equalizer" viewBox="0 0 920 170" aria-hidden="true">
      <g fill="var(--accent-deep)">
        <rect x="20"  y="140" width="16" height="30"/>
        <rect x="54"  y="110" width="16" height="60"/>
        <rect x="88"  y="80"  width="16" height="90"/>
        <rect x="122" y="125" width="16" height="45"/>
        <rect x="156" y="95"  width="16" height="75"/>
        <rect x="190" y="140" width="16" height="30"/>
        <rect x="224" y="115" width="16" height="55"/>
        <rect x="258" y="70"  width="16" height="100"/>
        <rect x="292" y="130" width="16" height="40"/>
        <rect x="326" y="100" width="16" height="70"/>
        <rect x="360" y="120" width="16" height="50"/>
        <rect x="394" y="60"  width="16" height="110"/>
        <rect x="428" y="135" width="16" height="35"/>
        <rect x="462" y="105" width="16" height="65"/>
        <rect x="496" y="85"  width="16" height="85"/>
        <rect x="530" y="125" width="16" height="45"/>
        <rect x="564" y="90"  width="16" height="80"/>
        <rect x="598" y="115" width="16" height="55"/>
        <rect x="632" y="75"  width="16" height="95"/>
        <rect x="666" y="130" width="16" height="40"/>
        <rect x="700" y="100" width="16" height="70"/>
        <rect x="734" y="120" width="16" height="50"/>
        <rect x="768" y="65"  width="16" height="105"/>
        <rect x="802" y="135" width="16" height="35"/>
        <rect x="836" y="95"  width="16" height="75"/>
        <rect x="870" y="115" width="16" height="55"/>
      </g>
    </svg>
  </section>

</body>
</html>
```